Etikett für ein Erfrischungsgetränk
Zielgruppe
Veltrano ist ein Startup Unternehmen, welches in naher Zukunft ein
Hibiskus-Erfrischungsgetränk auf den Markt bringen möchte.
Die Zielgruppe ist jedermann. Ob jung oder alt.
Aufgabenstellung
Das Etikett einer 0,33 l Longneckflasche soll:
Erfrischend, Modern aber auch Zeitlos, Einzigartig, dezent wirken.
Das Logo soll hervorstehen und der Hintergrund dezent sein.
Vorderetikett: 76 mm breit, 86 mm hoch
Rücketikett: 55 mm breit, 75 mm hoch
Die Getränkfarbe ist rötlich.

```html
<!DOCTYPE html>
<html lang="de">
<head>
<meta charset="utf-8">
<title>Veltrano – Etikett Erfrischungsgetränk</title>
<link rel="stylesheet" href="https://fonts.googleapis.com/css2?family=Arimo:wght@400;700&family=Patrick+Hand+SC&display=swap">
<style>
  :root {
    --page: #ffffff;
    --sky-deep: #7fd0ef;
    --sky-mid: #a9def4;
    --sky-light: #dff3fb;
    --lilac: #b9c8f0;
    --brand: #b0167e;
    --ink: #111111;
    --petal: #ec5f78;
    --petal-light: #f59aa8;
    --petal-core: #8a1030;
  }
  html, body {
    margin: 0;
    padding: 0;
    overflow: hidden;
    background: var(--page);
  }
  .canvas {
    position: relative;
    width: 1061px;
    height: 1200px;
    overflow: hidden;
    background: var(--page);
  }
  .label-shape {
    position: absolute;
    inset: 0;
  }
  .brand-name {
    position: absolute;
    left: 0;
    width: 1061px;
    top: 345px;
    margin: 0;
    text-align: center;
    font-family: "Arimo", sans-serif;
    font-weight: 700;
    font-size: 170px;
    line-height: 1;
    color: var(--brand);
  }
  .product-type {
    position: absolute;
    left: 224px;
    width: 566px;
    top: 708px;
    margin: 0;
    text-align: center;
    font-family: "Patrick Hand SC", cursive;
    font-size: 62px;
    line-height: 1;
    color: var(--ink);
    letter-spacing: 0.5px;
  }
  .product-detail {
    position: absolute;
    left: 230px;
    width: 570px;
    top: 782px;
    margin: 0;
    text-align: center;
    font-family: "Arimo", sans-serif;
    font-size: 35px;
    line-height: 1;
    color: var(--ink);
  }
  .flower-art {
    position: absolute;
    left: 395px;
    top: 842px;
    width: 223px;
    height: 231px;
    border-radius: 50%;
    background: radial-gradient(circle at 50% 50%, var(--petal-core) 0 10%, var(--petal) 30%, var(--petal-light) 75%, rgba(245,154,168,0) 100%);
  }
</style>
</head>
<body>
<main class="canvas">
  <svg class="label-shape" width="1061" height="1200" viewBox="0 0 1061 1200" aria-hidden="true">
    <defs>
      <linearGradient id="label-wash" x1="0" y1="0" x2="1" y2="1">
        <stop offset="0" stop-color="var(--sky-deep)"/>
        <stop offset="0.35" stop-color="var(--sky-mid)"/>
        <stop offset="0.6" stop-color="var(--lilac)"/>
        <stop offset="1" stop-color="var(--sky-light)"/>
      </linearGradient>
    </defs>
    <path d="M16 164 H224 C300 70 420 51 535 51 C650 51 770 70 845 164 H1051 V1200 H16 Z" fill="url(#label-wash)"/>
  </svg>

  <h1 class="brand-name">Veltrano</h1>

  <p class="product-type">Erfrischungsgetränk</p>
  <p class="product-detail">aus aufgebrühtem Hibiskustee</p>

  <div class="flower-art" role="img" aria-label="Illustration einer rosaroten Hibiskusblüte"></div>
</main>
</body>
</html>
```